Business card design for sports medicine and athlete care clinic.

We need a bold, solid business card design for our practitioners to stand out. We treat overuse & sports-related injuries and provide post-operative rehabilitation. Our specialisations include chronic conditions, men’s health, nutrition & musculoskeletal disorders (MSDs). All brand collateral in terms of fonts, logo and colour palette to be provided.

Target Market(s)

Athletes (professional and amateur), sportspeople, predominantly male

Industry/Entity Type

Health And Wellness

Contact Information for Business Card

The front of the card should be white with dark blue text the back dark blue with white text. The logo should be top-left. The business name should be horizontal and right of the logo. The tagline should be directly below centred on the back of the card (see top-banner.png and bottom-banner.png)

Font styles to use
Sans Serif

Colors
0355a3
0293ce
3176b5
ffffff
85acd3

Requirements
Nice to have
• Diagonal and/or horizontal line elements between logo and practitioner details and/or bottom corner of card (see slide.png and tag-bg.png).

```html
<!DOCTYPE html>
<html lang="en">
<head>
<meta charset="utf-8">
<title>The Stride Collective – Business Card</title>
<link href="https://fonts.googleapis.com/css2?family=Montserrat:wght@700;800&family=Mulish:wght@300;400;500&display=swap" rel="stylesheet">
<style>
  :root {
    --navy: #2f3656;
    --blue: #2f93c6;
    --sky: #33b1d8;
    --white: #ffffff;
    --paper: #f4f5f6;
    --backdrop: #e9eaec;
  }
  html, body {
    margin: 0;
    padding: 0;
    width: 1200px;
    height: 967px;
    overflow: hidden;
    background: var(--backdrop);
  }
  .canvas {
    position: relative;
    width: 1200px;
    height: 967px;
  }
  .card {
    position: absolute;
    left: 240px;
    width: 720px;
    height: 400px;
    overflow: hidden;
    box-shadow: 0 6px 18px rgba(0,0,0,0.12);
  }
  .card--front { top: 60px; background: var(--paper); }
  .card--back { top: 507px; background: var(--navy); }

  .accent-panel {
    position: absolute;
    left: 150px;
    top: 0;
    width: 110px;
    height: 400px;
    background: linear-gradient(90deg, var(--navy) 0%, var(--blue) 100%);
  }

  .brand {
    position: absolute;
    left: 300px;
    top: 62px;
    display: flex;
    align-items: center;
    gap: 12px;
  }
  .brand-dot {
    width: 26px;
    height: 26px;
    border-radius: 50%;
    background: var(--blue);
  }
  .brand-name {
    font-family: "Montserrat", sans-serif;
    font-weight: 800;
    font-size: 27px;
    color: var(--navy);
    line-height: 1;
  }
  .brand-tagline {
    position: absolute;
    left: 338px;
    top: 98px;
    font-family: "Mulish", sans-serif;
    font-weight: 500;
    font-size: 15px;
    color: var(--blue);
    letter-spacing: 0.2px;
    margin: 0;
  }

  .practitioner {
    position: absolute;
    left: 400px;
    top: 210px;
  }
  .practitioner-name {
    font-family: "Montserrat", sans-serif;
    font-weight: 800;
    font-size: 27px;
    color: var(--navy);
    margin: 0;
    line-height: 1.1;
  }
  .practitioner-credential {
    font-family: "Mulish", sans-serif;
    font-weight: 500;
    font-size: 20px;
    color: var(--blue);
    margin: 2px 0 14px;
  }
  .contact-list { list-style: none; margin: 0; padding: 0; }
  .contact-item {
    display: flex;
    align-items: center;
    gap: 10px;
    font-family: "Mulish", sans-serif;
    font-weight: 500;
    font-size: 18px;
    color: var(--navy);
    margin-bottom: 8px;
  }
  .contact-icon { width: 22px; height: 22px; flex: none; }

  .back-brand {
    position: absolute;
    left: 0; right: 0;
    top: 150px;
    display: flex;
    justify-content: center;
    align-items: center;
    gap: 12px;
  }
  .back-brand .brand-dot { background: var(--sky); }
  .back-brand .brand-name { color: var(--white); }
  .back-tagline {
    position: absolute;
    left: 0; right: 0;
    top: 210px;
    margin: 0;
    text-align: center;
    font-family: "Mulish", sans-serif;
    font-weight: 300;
    font-size: 17px;
    letter-spacing: 0.6px;
    color: var(--white);
  }
</style>
</head>
<body>
<main class="canvas">
  <section class="card card--front" aria-label="Card front">
    <div class="accent-panel" role="img" aria-label="Decorative diagonal bands in navy and blue"></div>

    <div class="brand">
      <span class="brand-dot"></span>
      <span class="brand-name">The Stride Collective</span>
    </div>
    <p class="brand-tagline">Sports medicine and athlete care</p>

    <div class="practitioner">
      <h1 class="practitioner-name">Dale WHITCOMBE</h1>
      <p class="practitioner-credential">DipRMT</p>
      <ul class="contact-list">
        <li class="contact-item">
          <svg class="contact-icon" viewBox="0 0 22 22" aria-hidden="true">
            <circle cx="11" cy="11" r="11" fill="var(--navy)"/>
            <path d="M7 6.5c.6-.6 1.4-.5 1.8.1l1 1.5c.3.5.2 1-.2 1.4l-.6.5c.5 1.1 1.4 2 2.5 2.5l.5-.6c.4-.4.9-.5 1.4-.2l1.5 1c.6.4.7 1.2.1 1.8l-.6.6c-.8.8-3 .4-5.1-1.7S6.2 8.1 7 7.3z" fill="var(--white)"/>
          </svg>
          02 9000 4127
        </li>
        <li class="contact-item">
          <svg class="contact-icon" viewBox="0 0 22 22" aria-hidden="true">
            <circle cx="11" cy="11" r="11" fill="var(--navy)"/>
            <rect x="5.5" y="7" width="11" height="8" rx="1" fill="var(--white)"/>
            <path d="M5.8 7.4 11 11.6l5.2-4.2" fill="none" stroke="var(--navy)" stroke-width="1.1"/>
          </svg>
          info@stridecollective.com.au
        </li>
        <li class="contact-item">
          <svg class="contact-icon" viewBox="0 0 22 22" aria-hidden="true">
            <circle cx="11" cy="11" r="11" fill="var(--navy)"/>
            <g fill="none" stroke="var(--white)" stroke-width="1">
              <circle cx="11" cy="11" r="5.5"/>
              <ellipse cx="11" cy="11" rx="2.4" ry="5.5"/>
              <path d="M5.5 11h11M6.3 8.2h9.4M6.3 13.8h9.4"/>
            </g>
          </svg>
          www.stridecollective.com.au
        </li>
      </ul>
    </div>
  </section>

  <section class="card card--back" aria-label="Card back">
    <div class="back-brand">
      <span class="brand-dot"></span>
      <span class="brand-name">The Stride Collective</span>
    </div>
    <p class="back-tagline">Delivering excellence in sports medicine and athlete care</p>
  </section>
</main>
</body>
</html>
```